Kelvo Rinn Computing Group - Need a Sales Promotion Flyer for a Managed IT Services company

We need a 4x9 (Front/Back) promotional sales flyer for a IT Consulting / Managed IT Services company.

Tailor the design after the uploaded logo and website screenshot.

Target Market(s)

Local Small Businesses

Industry/Entity Type

Information Technology

Other font styles liked:
• Sansation

Requirements
Must have
• Front of Flyer (Content):
• - Logo & Phone #
• - Tag Line: Your Local Technology Business Partner (Main Focus)
• - Text: Free IT Assessment (Main Focus)
• - Contact Information (Bottom)
• - Phone: 555.218.7391
• - Email: info@kelvorinnco.com
• - Web: www.kelvorinnco.com
• - Address: 482 N. Harlow St. / Suite 214
• Larkin CA 95512
• Back of Flyer:
• - Business Solutions
• - Managed IT Services
• - IT Consulting
• - About Us (Bottom)
• - Trusted Technology Partner
• - Client First
• - Industry Experts
• - Professional Staff
• - Latest Technologies
• Based in the beautiful Larkin Valley surrounded by the Sable Ridge mountains, Kelvo Rinn Computing Group is a trusted technology partner providing a wide range of business solutions, IT services, cloud services and IT consulting.

```html
<!DOCTYPE html>
<html lang="en">
<head>
<meta charset="utf-8">
<title>Kelvo Rinn Computing Group – Flyer Front and Back</title>
<link rel="stylesheet" href="https://fonts.googleapis.com/css2?family=Oswald:wght@500;600;700&family=Ubuntu:wght@400;700&display=swap">
<style>
  :root {
    --stage: #2c2c2c;
    --navy: #2b2770;
    --maroon: #8a1a1d;
    --orange: #f7901e;
    --plum: #7c2150;
    --yellow: #d8cc1f;
    --gold: #e7c84a;
    --lime: #a3be37;
    --brown: #5e5548;
    --logo-orange: #e0823c;
    --ink: #1d1d1d;
    --white: #ffffff;
    --slate: #6e6a62;
  }
  * { box-sizing: border-box; margin: 0; padding: 0; }
  html, body { width: 1200px; height: 1200px; overflow: hidden; background: var(--stage); }
  body { position: relative; font-family: "Ubuntu", sans-serif; color: var(--white); }

  .flyer { position: absolute; display: flex; flex-direction: column; }
  .flyer--back { left: 77px; top: 128px; width: 470px; }
  .flyer--front { left: 659px; top: 130px; width: 475px; }

  .band { display: flex; align-items: center; justify-content: center; text-align: center; }
  .condensed { font-family: "Oswald", sans-serif; font-weight: 600; text-transform: uppercase; }

  /* Back side */
  .top-bar { height: 58px; background: var(--navy); font-size: 30px; letter-spacing: 0.2px; }
  .brand-panel { background: var(--white); flex-direction: column; gap: 10px; }
  .brand-panel--back { height: 222px; }
  .brand-name { display: flex; align-items: center; gap: 14px; font-family: "Ubuntu", sans-serif; font-weight: 700; color: var(--brown); line-height: 1.05; text-align: left; }
  .brand-name__dot { flex: none; border-radius: 50%; background: var(--logo-orange); }
  .brand-panel--back .brand-name { font-size: 34px; }
  .brand-panel--back .brand-name__dot { width: 30px; height: 30px; }

  .section-title { height: 49px; background: var(--orange); font-size: 27px; }
  .section-title--about { height: 52px; }
  .services { height: 187px; background: var(--maroon); gap: 28px; }
  .hex { width: 122px; height: 100px; background: var(--yellow); clip-path: polygon(25% 0, 75% 0, 100% 50%, 75% 100%, 25% 100%, 0 50%);
         display: flex; align-items: center; justify-content: center; color: var(--ink); font-size: 16px; line-height: 1.45; font-weight: 500; }
  .copy { background: var(--maroon); font-size: 17px; line-height: 1.35; padding: 0 10px; white-space: nowrap; }
  .copy--intro { height: 120px; }
  .copy--story { height: 134px; font-size: 16.5px; }
  .copy strong { font-weight: 700; }
  .values { height: 102px; display: grid; grid-template-columns: 1fr 1fr; grid-template-rows: 1fr 1fr; }
  .value { display: flex; align-items: center; justify-content: center; font-size: 17px; font-weight: 500; }
  .value--orange { background: var(--orange); }
  .value--plum { background: var(--plum); }

  .web-bar { height: 54px; background: var(--navy); gap: 22px; font-weight: 700; font-size: 26px; }
  .globe { width: 36px; height: 36px; }

  /* Front side */
  .brand-panel--front { height: 193px; }
  .brand-panel--front .brand-name { font-size: 38px; }
  .brand-panel--front .brand-name__dot { width: 32px; height: 32px; }
  .tagline { height: 34px; background: var(--maroon); color: var(--gold); font-size: 19px; }
  .call-bar { height: 57px; background: var(--lime); color: var(--ink); gap: 22px; font-size: 31px; }
  .call-bar__icon { width: 46px; height: 46px; }
  .hero { height: 302px; background: linear-gradient(135deg, #3a4a5e 0%, #8e9fb3 45%, #5a6473 75%, #2a2c36 100%); }
  .offer { height: 102px; background: linear-gradient(180deg, #1c2340, #121629); font-family: "Oswald", sans-serif; font-weight: 700;
           font-size: 52px; color: var(--gold); letter-spacing: 0.5px; text-transform: uppercase; }
  .contact { height: 217px; display: flex; }
  .contact__info { width: 238px; background: var(--maroon); display: flex; flex-direction: column; }
  .contact__title { color: var(--gold); font-size: 24px; text-align: center; padding-top: 10px; }
  .contact__rule { height: 2px; background: #3f8ac9; margin: 8px 22px 0 21px; }
  .contact__row { display: flex; gap: 10px; padding: 0 12px; font-size: 12.5px; line-height: 1.6; }
  .contact__row--address { margin-top: 14px; }
  .contact__row--email { margin-top: 14px; align-items: center; }
  .contact__icon { width: 18px; height: 18px; flex: none; margin-top: 2px; }
  .contact__phone { margin-top: auto; height: 38px; background: var(--slate); display: flex; align-items: center; gap: 12px; padding-left: 12px; font-size: 25px; }
  .contact__phone svg { width: 28px; height: 28px; }
  .booking { flex: 1; background: var(--orange); color: var(--ink); flex-direction: column; font-size: 22px; line-height: 1.3; padding: 0 6px; }
  .booking strong { font-weight: 700; }
  .booking__gap { height: 10px; }
</style>
</head>
<body>

<svg width="0" height="0" style="position:absolute">
  <defs>
    <symbol id="icon-phone" viewBox="0 0 24 24">
      <path d="M6.6 10.8a15.1 15.1 0 0 0 6.6 6.6l2.2-2.2c.3-.3.7-.4 1-.2 1.1.4 2.3.6 3.6.6.6 0 1 .4 1 1V20c0 .6-.4 1-1 1A17 17 0 0 1 3 4c0-.6.4-1 1-1h3.5c.6 0 1 .4 1 1 0 1.3.2 2.5.6 3.6.1.3 0 .7-.2 1z" fill="currentColor"/>
    </symbol>
    <symbol id="icon-globe" viewBox="0 0 40 40">
      <g fill="none" stroke="#c7854a" stroke-width="2">
        <circle cx="20" cy="20" r="17"/><ellipse cx="20" cy="20" rx="8" ry="17"/>
        <line x1="3" y1="20" x2="37" y2="20"/><line x1="20" y1="3" x2="20" y2="37"/>
        <path d="M6 11h28M6 29h28"/>
      </g>
    </symbol>
  </defs>
</svg>

<!-- Back side -->
<section class="flyer flyer--back" aria-label="Flyer back side">
  <header class="band top-bar condensed">Kelvo Rinn Computing Group</header>
  <div class="band brand-panel brand-panel--back">
    <div class="brand-name"><span class="brand-name__dot"></span><span>Kelvo Rinn<br>Computing Group</span></div>
  </div>
  <h2 class="band section-title condensed">Our Services</h2>
  <div class="band services">
    <div class="hex condensed">Managed<br>IT Services</div>
    <div class="hex condensed">Business<br>Solutions</div>
    <div class="hex condensed">IT<br>Consulting</div>
  </div>
  <h2 class="band section-title section-title--about condensed">About Us</h2>
  <p class="band copy copy--intro"><span>We will help you connect your business with the<br><strong>latest technologies using a comprehensive set of<br>IT services and business solutions</strong> to improve<br>business performance and IT agility.</span></p>
  <div class="values condensed">
    <div class="value value--orange">Trusted Technology Partner</div>
    <div class="value value--plum">Client First</div>
    <div class="value value--plum">Industry Experts</div>
    <div class="value value--orange">Professional Staff</div>
  </div>
  <p class="band copy copy--story"><span>Based in the beautiful Larkin Valley surrounded by the<br>Sable Ridge mountains, Kelvo Rinn Computing Group<br>is a trusted technology partner providing a wide range<br>of business solutions, IT services, cloud services<br>and IT consulting.</span></p>
  <footer class="band web-bar"><svg class="globe"><use href="#icon-globe"/></svg><span>www.kelvorinnco.com</span></footer>
</section>

<!-- Front side -->
<section class="flyer flyer--front" aria-label="Flyer front side">
  <div class="band brand-panel brand-panel--front">
    <div class="brand-name"><span class="brand-name__dot"></span><span>Kelvo Rinn<br>Computing Group</span></div>
  </div>
  <div class="band tagline condensed">Your Local Technology Business Partner</div>
  <div class="band call-bar condensed">
    <span>Call Us</span>
    <svg class="call-bar__icon" viewBox="0 0 46 46"><circle cx="23" cy="23" r="20" fill="none" stroke="#1d1d1d" stroke-width="3"/><use href="#icon-phone" x="11" y="11" width="24" height="24" color="#1d1d1d"/></svg>
    <span>555-218-7391</span>
  </div>
  <div class="hero" role="img" aria-label="Photo of a businessman holding out an open hand with floating cloud and device network icons in front of a server room"></div>
  <div class="band offer">Free IT Assessment</div>
  <div class="contact">
    <div class="contact__info">
      <h3 class="contact__title condensed">Contact Us</h3>
      <div class="contact__rule"></div>
      <div class="contact__row contact__row--address">
        <svg class="contact__icon" viewBox="0 0 24 24"><path d="M12 2a7 7 0 0 0-7 7c0 5 7 13 7 13s7-8 7-13a7 7 0 0 0-7-7zm0 9.5a2.5 2.5 0 1 1 0-5 2.5 2.5 0 0 1 0 5z" fill="#a3be37"/></svg>
        <span>ADDRESS<br>482 N. Harlow St. / Suite 214<br>Larkin CA 95512</span>
      </div>
      <div class="contact__row contact__row--email">
        <svg class="contact__icon" viewBox="0 0 24 24"><circle cx="12" cy="12" r="11" fill="#3fa2e0"/><path d="M9 14l6-4" stroke="#fff" stroke-width="2"/></svg>
        <span>info@kelvorinnco.com</span>
      </div>
      <div class="contact__phone condensed">
        <svg viewBox="0 0 28 28"><circle cx="14" cy="14" r="12" fill="none" stroke="#1d1d1d" stroke-width="2"/><use href="#icon-phone" x="7" y="7" width="14" height="14" color="#1d1d1d"/></svg>
        <span>555-218-7391</span>
      </div>
    </div>
    <div class="band booking">
      <span>To Book Your</span>
      <strong>FREE Technology<br>Assessment</strong>
      <span class="booking__gap"></span>
      <strong>Visit Our Website<br>or</strong>
      <strong>Call Us Today</strong>
    </div>
  </div>
  <footer class="band web-bar"><svg class="globe"><use href="#icon-globe"/></svg><span>www.kelvorinnco.com</span></footer>
</section>

</body>
</html>
```